Boutique Wealth management firm needs a new business card design

I want to update my business card design to be more consistent with the look and feel of my website (www.corvalen-capital.example). I would like to incorporate an ivory parchment background and am open to switching from the current "portrait" layout to a more traditional "landscape" orientation. The final design should convey stability and exclusivity and I want something in PDF format that is ready to send to the printer
Updates

Thank you all for taking the time to submit your designs for my project. I've made my decision and picked the design I like best. Thanks again!

Industry/Entity Type

Business

```html
<!DOCTYPE html>
<html lang="en">
<head>
<meta charset="utf-8">
<title>Corvalen Wealth Advisory – Business Card</title>
<link href="https://fonts.googleapis.com/css2?family=Open+Sans:wght@400;700&display=swap" rel="stylesheet">
<style>
  :root {
    --backdrop: #e6e2da;
    --ivory: #f7f1e1;
    --ivory-shade: #ece3cc;
    --maroon: #7d2350;
    --maroon-deep: #4a1630;
    --ink: #1c1c1c;
    --text: #4a4a4a;
  }
  * { box-sizing: border-box; margin: 0; padding: 0; }
  html, body { width: 1200px; height: 828px; overflow: hidden; }
  body {
    background: var(--backdrop);
    font-family: "Open Sans", Arial, sans-serif;
    display: flex;
    align-items: center;
    justify-content: center;
    gap: 60px;
  }
  .card {
    position: relative;
    width: 525px;
    height: 300px;
    background: radial-gradient(ellipse at 40% 35%, var(--ivory) 55%, var(--ivory-shade) 100%);
    box-shadow: 0 6px 18px rgba(0,0,0,0.18);
    overflow: hidden;
  }
  .brand {
    position: absolute;
    color: var(--maroon);
    font-weight: 700;
    font-size: 24px;
    line-height: 1;
    white-space: nowrap;
  }
  .card-front .brand {
    left: 50%;
    top: 50%;
    transform: translate(-50%, -50%);
  }
  .card-back .brand {
    right: 70px;
    top: 50px;
    font-size: 20px;
  }
  .corner-art {
    position: absolute;
    right: 0;
    bottom: 0;
    width: 260px;
    height: 190px;
    background: linear-gradient(135deg, var(--maroon-deep), var(--maroon));
    border-top-left-radius: 100% 100%;
  }
  .contact {
    position: absolute;
    left: 34px;
    top: 120px;
    color: var(--text);
    font-size: 12px;
    line-height: 1.45;
  }
  .contact-name {
    color: var(--maroon);
    font-weight: 700;
    font-size: 15px;
    letter-spacing: 0.5px;
  }
  .contact-role { margin-bottom: 14px; }
  .contact-address { margin-bottom: 14px; }
  .contact-list { list-style: none; }
  .contact-list li { display: flex; align-items: center; gap: 6px; }
  .contact-list svg { width: 10px; height: 10px; fill: var(--ink); flex: none; }
</style>
</head>
<body>
  <section class="card card-front" aria-label="Card front">
    <p class="brand">Corvalen Wealth Advisory</p>
  </section>

  <section class="card card-back" aria-label="Card back">
    <div class="corner-art" role="img" aria-label="Decorative curved swoosh in maroon and black"></div>

    <p class="brand">Corvalen Wealth Advisory</p>

    <div class="contact">
      <p class="contact-name">DANIEL ASHFORD</p>
      <p class="contact-role">Managing Director</p>
      <p class="contact-address">24 Harbour Lane, 9th Floor<br>Westbrook</p>
      <ul class="contact-list">
        <li><svg viewBox="0 0 10 10"><path d="M2 0.5 L3.8 2.8 L2.8 3.9 C3.4 5.2 4.8 6.6 6.1 7.2 L7.2 6.2 L9.5 8 L8.3 9.5 C4.5 9.2 0.8 5.5 0.5 1.7 Z"/></svg>012 555 0148</li>
        <li><svg viewBox="0 0 10 10"><rect x="0.5" y="2" width="9" height="6.5"/></svg>info@corvalen.example</li>
        <li><svg viewBox="0 0 10 10"><circle cx="5" cy="5" r="4.5"/></svg>www.corvalen-capital.example</li>
      </ul>
    </div>
  </section>
</body>
</html>
```